Super elegant, crisp & clean Business card design required

We recently upgraded our branding - which is on our website - tavorelstudio.com

I would like a simple, yet elegant, clean business card design please.

The font of my logo is Cinzel - and because of the natural colour - it's best to have this on a black background.

I would like to have the back of the business card - with simply my logo.

PLEASE DO NOT SUBMIT A COMPLICATED / UNCLEAN DESIGN

Industry/Entity Type

Business

Contact Information for Business Card

Dalvik Ostrander Photography

Font styles to use
Other font styles liked:
• Cinzel

Requirements
Must have
• A backpage with nothing but my logo
• Simple design - stands out
Should not have
• Colour that dont align with my logo
• Over complicated '/ non symmetrical design

```html
<!DOCTYPE html>
<html lang="en">
<head>
<meta charset="utf-8">
<title>Dalvik Ostrander Photography – Business Cards</title>
<link rel="stylesheet" href="https://fonts.googleapis.com/css2?family=Cinzel:wght@400;500&family=Lato:wght@300;400&display=swap">
<style>
  :root {
    --stage: #1b1b1b;
    --paper: #ffffff;
    --ink-dark: #1f1f1f;
    --gold: #a59b7e;
    --gold-text: #9a8c69;
    --text: #2a2a2a;
    --muted: #555555;
  }
  * { box-sizing: border-box; margin: 0; padding: 0; }
  html, body {
    width: 1200px; height: 922px; overflow: hidden;
    background: var(--stage);
  }
  .canvas { position: relative; width: 1200px; height: 922px; }

  .card {
    position: absolute;
    width: 620px; height: 354px;
    border-radius: 16px;
    overflow: hidden;
    background: var(--paper);
  }

  /* Logo side */
  .card--logo { left: 60px; top: 90px; }
  .brand {
    position: absolute; inset: 0;
    display: flex; flex-direction: column; align-items: center; justify-content: center;
    color: var(--gold-text);
    font-family: "Cinzel", serif;
  }
  .brand__mark {
    width: 64px; height: 64px; border-radius: 50%;
    border: 2px solid var(--gold-text);
    margin-bottom: 26px;
  }
  .brand__name { font-size: 32px; font-weight: 400; letter-spacing: 1px; line-height: 1; }
  .brand__tag { font-size: 13px; letter-spacing: 9px; margin-top: 8px; padding-left: 9px; }

  /* Contact side */
  .card--contact { left: 520px; top: 478px; }
  .edge-strip { position: absolute; left: 0; top: 0; bottom: 0; width: 22px; background: var(--gold); }
  .dark-panel { position: absolute; left: 22px; top: 0; bottom: 0; width: 246px; background: var(--ink-dark); }
  .dark-panel .brand__mark { width: 44px; height: 44px; margin-bottom: 18px; }
  .dark-panel .brand__name { font-size: 19px; }
  .dark-panel .brand__tag { font-size: 9px; letter-spacing: 6px; padding-left: 6px; margin-top: 6px; }
  .gold-band { position: absolute; left: 268px; top: 0; bottom: 0; width: 30px; background: var(--gold); }

  .icon {
    position: absolute; left: 263px;
    width: 40px; height: 40px; border-radius: 50%;
    background: var(--gold);
    display: flex; align-items: center; justify-content: center;
  }
  .icon--person { top: 42px; border: 3px solid var(--paper); }
  .icon--small { width: 22px; height: 22px; left: 272px; background: none; }

  .holder { position: absolute; left: 322px; top: 46px; color: var(--text); }
  .holder__name { font-family: "Cinzel", serif; font-size: 19px; letter-spacing: 2px; line-height: 1.1; }
  .holder__role { font-family: "Cinzel", serif; font-size: 11px; letter-spacing: 2px; color: var(--muted); margin-top: 2px; }

  .contacts { position: absolute; left: 322px; top: 218px; list-style: none; }
  .contacts li {
    font-family: "Lato", sans-serif; font-weight: 400;
    font-size: 14px; letter-spacing: 1.2px; color: var(--text);
    height: 30px; line-height: 22px;
  }
</style>
</head>
<body>
<main class="canvas">

  <section class="card card--logo" aria-label="Business card front">
    <div class="brand">
      <span class="brand__mark" aria-hidden="true"></span>
      <span class="brand__name">Dalvik Ostrander</span>
      <span class="brand__tag">PHOTOGRAPHY</span>
    </div>
  </section>

  <section class="card card--contact" aria-label="Business card back">
    <div class="edge-strip"></div>
    <div class="dark-panel">
      <div class="brand">
        <span class="brand__mark" aria-hidden="true"></span>
        <span class="brand__name">Dalvik Ostrander</span>
        <span class="brand__tag">PHOTOGRAPHY</span>
      </div>
    </div>
    <div class="gold-band"></div>

    <span class="icon icon--person" aria-hidden="true"></span>
    <div class="holder">
      <p class="holder__name">Dalvik Ostrander</p>
      <p class="holder__role">Owner</p>
    </div>

    <span class="icon icon--small" style="top:218px" aria-hidden="true">
      <svg width="14" height="18" viewBox="0 0 14 18"><rect x="1" y="1" width="12" height="16" rx="2" fill="none" stroke="#fff" stroke-width="1.6"/><rect x="3.5" y="3.5" width="7" height="5" fill="#fff"/></svg>
    </span>
    <span class="icon icon--small" style="top:248px" aria-hidden="true">
      <svg width="18" height="14" viewBox="0 0 18 14"><rect x="1" y="1" width="16" height="12" rx="1.5" fill="none" stroke="#fff" stroke-width="1.6"/><path d="M1 2 L9 8 L17 2" fill="none" stroke="#fff" stroke-width="1.6"/></svg>
    </span>
    <span class="icon icon--small" style="top:278px" aria-hidden="true">
      <svg width="16" height="16" viewBox="0 0 16 16"><circle cx="8" cy="8" r="6.8" fill="none" stroke="#fff" stroke-width="1.6"/><ellipse cx="8" cy="8" rx="3" ry="6.8" fill="none" stroke="#fff" stroke-width="1.2"/><path d="M1.2 8 H14.8" stroke="#fff" stroke-width="1.2"/></svg>
    </span>

    <ul class="contacts">
      <li>07946 218830</li>
      <li>www.tavorelstudio.com</li>
      <li>info@tavorelstudio.com</li>
    </ul>
  </section>

</main>
</body>
</html>
```